Pamphlet for introducing people to our church

I would like a church pamphlet designed, that includes the content in file "tovik-pamphlet.txt".

I am looking for a design that will incorporate the content in a professional and creative manner.

You do not have to use the content in any specific order, but I am relying on your skill and design knowledge to organize everything in an artistic and effective way.

Target Market(s)

Everyone

Industry/Entity Type

Religious

Requirements
Must have
• logo, use of content provided, use of branding (logo colors)
Nice to have
• More images where necessary
Should not have
• cross

```html
<!DOCTYPE html>
<html lang="en">
<head>
<meta charset="utf-8">
<title>Tovik — Church Pamphlet</title>
<link rel="stylesheet" href="https://fonts.googleapis.com/css2?family=Arimo:wght@400;700&family=Cinzel:wght@400&display=swap">
<style>
  :root{
    --navy:#12385e;
    --navy-deep:#0f2f52;
    --orange:#e8891e;
    --paper:#ffffff;
    --stage:#e9ebee;
    --ink:#1c1c1c;
    --sky-top:#7fa6cf;
    --sky-mid:#b9d0e6;
    --sky-low:#dfe9f3;
    --sunset-dark:#2a1a10;
    --sunset-warm:#8a5a2a;
    --sunset-glow:#c58a45;
  }
  *{box-sizing:border-box;margin:0;padding:0}
  html,body{width:1200px;height:900px;overflow:hidden;background:var(--stage)}
  body{position:relative;font-family:"Arimo",Arial,sans-serif;color:var(--ink)}

  /* ---------- brand name ---------- */
  .brand{position:absolute;display:flex;align-items:center;gap:8px;font-family:"Arimo",Arial,sans-serif;font-weight:700;color:var(--navy);line-height:1;letter-spacing:1px}
  .brand__dot{border-radius:50%;background:var(--navy)}

  /* ---------- front cover ---------- */
  .cover{position:absolute;left:45px;top:195px;width:350px;height:510px;background:var(--paper);overflow:hidden;box-shadow:0 6px 18px rgba(0,0,0,.18)}
  .cover__bar{position:absolute;left:0;width:100%;background:var(--orange)}
  .cover__bar--top{top:0;height:14px}
  .cover__bar--bottom{bottom:0;height:8px}
  .cover .brand{left:40px;top:110px;font-size:30px}
  .cover .brand__dot{width:12px;height:12px}
  .cover__photo{position:absolute;left:0;top:210px;width:350px;height:250px}
  .cover__url{position:absolute;right:40px;bottom:22px;font-weight:700;font-size:10.5px;color:var(--navy)}

  /* ---------- inside spread ---------- */
  .spread{position:absolute;left:435px;top:195px;width:720px;height:510px;overflow:hidden;box-shadow:0 6px 18px rgba(0,0,0,.18)}
  .spread__sky{position:absolute;inset:0}
  .spread__fold{position:absolute;left:360px;top:0;width:1px;height:455px;background:rgba(255,255,255,.35)}
  .spread__band{position:absolute;left:0;bottom:0;width:100%;height:55px;background:var(--navy-deep)}
  .page{position:absolute;top:0;width:360px;height:455px}
  .page--left{left:0}
  .page--right{left:360px}
  .page .brand{left:56px;top:44px;font-size:22px}
  .page .brand__dot{width:9px;height:9px}

  .mission{position:absolute;left:56px;top:122px;width:268px;font-size:9.2px;line-height:1.33;text-align:justify}
  .mission__title{font-weight:700;font-size:9.5px;margin-bottom:14px}
  .mission p.gap{margin-top:12px}

  .programs{position:absolute;left:38px;top:43px;width:272px}
  .program{margin-bottom:10px}
  .program__title{font-weight:700;font-size:10px;color:var(--navy-deep);letter-spacing:.2px}
  .program__text{font-size:9.2px;line-height:1.25}

  .motto{position:absolute;right:18px;top:312px;width:140px;font-family:"Cinzel",serif;font-size:25px;line-height:.96;color:#fff;text-align:center;letter-spacing:.5px}
  .contact{position:absolute;left:398px;bottom:12px;font-size:8.4px;color:#fff;line-height:1.35}
  .contact b{font-weight:700}
</style>
</head>
<body>

<section class="cover">
  <div class="cover__bar cover__bar--top"></div>
  <div class="brand"><span class="brand__dot"></span>TOVIK</div>
  <svg class="cover__photo" viewBox="0 0 350 250" preserveAspectRatio="none" role="img" aria-label="Photograph: silhouette of a person with arms raised against a golden sunset sky">
    <defs>
      <linearGradient id="sunset" x1="0" y1="0" x2="0" y2="1">
        <stop offset="0" stop-color="var(--sunset-dark)"/>
        <stop offset=".45" stop-color="var(--sunset-warm)"/>
        <stop offset=".7" stop-color="var(--sunset-glow)"/>
        <stop offset="1" stop-color="var(--sunset-dark)"/>
      </linearGradient>
    </defs>
    <rect width="350" height="250" fill="url(#sunset)"/>
  </svg>
  <div class="cover__url">www.tovik.org</div>
  <div class="cover__bar cover__bar--bottom"></div>
</section>

<section class="spread">
  <svg class="spread__sky" viewBox="0 0 720 510" role="img" aria-label="Photograph: bright blue sky with clouds, a silhouette of a girl with flowing hair and birds taking flight on the right page">
    <defs>
      <linearGradient id="sky" x1="0" y1="0" x2="0" y2="1">
        <stop offset="0" stop-color="var(--sky-top)"/>
        <stop offset=".5" stop-color="var(--sky-mid)"/>
        <stop offset=".85" stop-color="var(--sky-low)"/>
      </linearGradient>
    </defs>
    <rect width="720" height="510" fill="url(#sky)"/>
  </svg>
  <div class="spread__fold"></div>

  <div class="page page--left">
    <div class="brand"><span class="brand__dot"></span>TOVIK</div>
    <div class="mission">
      <h2 class="mission__title">MISSION STATEMENT:</h2>
      <p>TOVIK is a gathering of believers whose purpose is to seek the face of God for an authentic restoration of the church as a body of born again believers around the world.</p>
      <p class="gap">As a gathering of believers, TOVIK seeks an awakening of the mind founded on the precepts and teachings of Jesus Christ.</p>
      <p>The modern church has replaced the simple and Kingdom centered principles of Jesus’s disciples with complacent and compromised teachings on earthly prosperity.</p>
      <p>We believe in humbly seeking God without motive to use God or His Word for our own gain. The end times church will experience a glorious revival, renewed love and zeal for true discipleship, faith, and godliness as Jesus intended for us.</p>
    </div>
  </div>

  <div class="page page--right">
    <div class="programs">
      <div class="program">
        <h3 class="program__title">MINISTRIES</h3>
        <p class="program__text">Kingdom seeds (Children's ministry)Children learn to be seeds of godliness in the world.</p>
      </div>
      <div class="program">
        <h3 class="program__title">SCHOOL OF PILGRIMS</h3>
        <p class="program__text">Learn the basics of Christian faith and about God's purpose for your life.</p>
      </div>
      <div class="program">
        <h3 class="program__title">SCHOOL OF DISCIPLES</h3>
        <p class="program__text">Deepen your knowledge of God's word and learn how to server him.</p>
      </div>
    </div>
    <div class="motto">A<br>Voice<br>to<br>all<br>nation</div>
  </div>

  <div class="spread__band"></div>
  <p class="contact">If you need prayer or counseling give us a call at <b>+1 555-014-2277</b><br>or email us at <b>hello@cedarhollow.org</b></p>
</section>

</body>
</html>
```